Clockharbor Homepage Banner 1060 W x 100 H

Please see the attached 'word' document (Also copied below)
Feel free to use any images or logos from our website.
www.clockharbor.com.au

Background:
We are an Australian based official watch distributor/online retailer of international watch brands.

We require a new banner ad (1060 W x 100 H) to replace the existing one on our homepage www.clockharbor.com.au & wish to convey the following information:
*(Please feel free to alter wording, include or exclude points below & generally take creative license (with commercial reality in mind). We sell some luxury watches, so it must look professional & maintain a luxury look & feel.)

Clockharbor Direct:
Revolutionising the retail watch market !

- Buy direct from the official distributor & get world competitive
online prices (with full international warranty, & all original
papers, box & invoice)

- Eliminate all risk of fakes & non-existent factory warranty from
'grey' market sellers

- Free worldwide delivery over A$300

- Order online & 'try-on' in the comfort of your own home.
If you're not 100% happy, just post it back for a full refund or
exchange within 30 days

- Prefer to see & try on before purchase? Visit one of our retail
partner stores.

*** Feel free to copy any images from our website
www.clockharbor.com.au
Updates

Target Market(s)

Luxury watches

Industry/Entity Type

Retail

Font styles to use
Sans Serif

Requirements
Must have
• Visual imagery, text
Nice to have
• Feel free to use your creativity...
Should not have
• Cheap looking or tacky images. We sell some luxury watches, so we need to keep a professional & luxury image.

```html
<!DOCTYPE html>
<html lang="en">
<head>
<meta charset="utf-8">
<title>Clockharbor Direct – Homepage Banner</title>
<link rel="stylesheet" href="https://fonts.googleapis.com/css2?family=Roboto+Condensed:wght@400;700&family=Roboto:wght@400;500&display=swap">
<style>
  :root {
    --night: #0d0d0d;
    --night-soft: #2a2622;
    --gold: #d3a64a;
    --gold-light: #e6bf68;
    --white: #ffffff;
    --grey: #d8d8d8;
  }
  * { margin: 0; padding: 0; box-sizing: border-box; }
  html, body { width: 1200px; height: 113px; overflow: hidden; background: var(--night); }
  .banner {
    position: relative;
    width: 1200px; height: 113px; overflow: hidden;
    background: linear-gradient(90deg, #1a1714 0%, #0c0c0c 30%, #151310 65%, #0c0c0c 100%);
    font-family: "Roboto", Arial, sans-serif;
    color: var(--white);
  }
  .city-backdrop {
    position: absolute; inset: 0;
    background:
      linear-gradient(180deg, rgba(60,52,44,.55) 0%, rgba(20,18,16,.2) 45%, rgba(70,58,44,.45) 100%),
      linear-gradient(90deg, rgba(90,78,62,.35) 0%, rgba(0,0,0,0) 40%, rgba(80,70,56,.3) 80%);
  }
  .offer {
    position: absolute; left: 48px; top: 22px;
    font-family: "Roboto Condensed", Arial, sans-serif;
    color: var(--gold);
    line-height: 1;
  }
  .offer-lead, .offer-tail { font-size: 17px; font-weight: 400; }
  .offer-lead { text-transform: uppercase; letter-spacing: .3px; }
  .offer-main {
    font-size: 24px; font-weight: 700; text-transform: uppercase;
    color: var(--gold-light); margin: 2px 0 3px; letter-spacing: .2px;
  }
  .promise {
    position: absolute; left: 374px; width: 556px; top: 14px;
    text-align: center;
  }
  .promise-title { font-size: 16px; font-weight: 500; line-height: 1.2; }
  .promise-sub { font-size: 12.5px; color: var(--grey); margin-top: 2px; }
  .divider {
    position: absolute; left: 374px; top: 56px; width: 556px; height: 1px;
    background: var(--gold);
  }
  .benefit {
    position: absolute; top: 68px;
    display: flex; align-items: flex-start; gap: 10px;
    font-size: 10.5px; line-height: 1.2; text-transform: uppercase; color: var(--grey);
  }
  .benefit svg { width: 22px; height: 22px; flex: none; stroke: var(--gold); fill: none; stroke-width: 1.4; }
  .benefit-delivery { left: 374px; }
  .benefit-refund { left: 557px; }
  .benefit-genuine { left: 741px; }
  .watch-visual {
    position: absolute; left: 968px; top: -110px;
    width: 300px; height: 300px; border-radius: 50%;
    background: radial-gradient(circle at 40% 45%, #2b2b2b 0%, #151515 45%, #8c8c8c 47%, #d9d9d9 50%, #6a6a6a 53%, #1a1a1a 56%);
  }
</style>
</head>
<body>
  <div class="banner">
    <div class="city-backdrop" role="img" aria-label="Dusky city skyline at night in warm tones"></div>

    <div class="offer">
      <p class="offer-lead">Buy direct from the</p>
      <p class="offer-main">Official Distributor</p>
      <p class="offer-tail">&amp; get world competitive online prices</p>
    </div>

    <div class="promise">
      <p class="promise-title">Order online &amp; 'try-on' in the comfort of your own home...</p>
      <p class="promise-sub">or prefer to see &amp; try on before purchase? Visit one of our retail partner stores!</p>
    </div>

    <div class="divider"></div>

    <div class="benefit benefit-delivery">
      <svg viewBox="0 0 22 22" aria-hidden="true"><path d="M3 7 11 3l8 4v9l-8 4-8-4z"/><path d="M3 7l8 4 8-4M11 11v9"/></svg>
      <p>Free worldwide delivery<br>over A$300</p>
    </div>

    <div class="benefit benefit-refund">
      <svg viewBox="0 0 22 22" aria-hidden="true"><path d="M18 8a8 8 0 1 0 1 5"/><path d="M19 3v5h-5"/><path d="M13 8.5h-2.5a1.5 1.5 0 0 0 0 3h1a1.5 1.5 0 0 1 0 3H9M11 7v1.5M11 14.5V16"/></svg>
      <p>Full refund or exchange<br>within 30 days</p>
    </div>

    <div class="benefit benefit-genuine">
      <svg viewBox="0 0 22 22" aria-hidden="true"><path d="M5 2h9l3 3v15H5z"/><path d="M8 8h6M8 11h6M8 14h4"/></svg>
      <p>Eliminate all risk of fakes &amp;<br>non-existent factory warranty</p>
    </div>

    <div class="watch-visual" role="img" aria-label="Close-up of a luxury pilot wristwatch with black dial"></div>
  </div>
</body>
</html>
```